Property risk and finance brokerage company needs a business card design

Tarlow Financial requires a business card design. Please integrate existing logo (refer uploaded file).
hex codes used on logo #002649 #008ED6 #444F51 #ADAFAA
font used - Cinzel
Contact information
Renata Sollisford
Director
Mobile: 0491 738 205
email: r.sollisford@tarlowfinancial.example.au
website: www.tarlowfinancial.example.au
CRN : 918354
PO Box 527
Larkvale, Victoria, 3999
Horizontal orientation please
Finance

```html
<!DOCTYPE html>
<html lang="en">
<head>
<meta charset="utf-8">
<title>Tarlow Financial – Business Card</title>
<link rel="stylesheet" href="https://fonts.googleapis.com/css2?family=Cinzel:wght@400&family=Montserrat:wght@400;500&display=swap">
<style>
  :root {
    --navy: #002649;
    --blue: #008ED6;
    --mid-blue: #0b5ea3;
    --slate: #444F51;
    --silver: #ADAFAA;
    --paper: #ffffff;
    --backdrop-light: #c9c9c9;
    --backdrop-dark: #9e9e9e;
  }
  * { box-sizing: border-box; margin: 0; padding: 0; }
  html, body { width: 1200px; height: 900px; overflow: hidden; }
  body {
    background: radial-gradient(ellipse at 50% 40%, var(--backdrop-light), var(--backdrop-dark));
    position: relative;
    font-family: "Montserrat", Arial, sans-serif;
  }
  .card {
    position: absolute;
    width: 540px;
    height: 312px;
    border-radius: 26px;
    box-shadow: 0 10px 26px rgba(0,0,0,0.28);
    overflow: hidden;
  }

  /* Front */
  .card-front {
    left: 370px; top: 105px;
    background: linear-gradient(135deg, var(--mid-blue) 0%, #063a6f 55%, var(--navy) 100%);
    color: var(--paper);
  }
  .front-brand {
    position: absolute;
    left: 0; right: 0; top: 96px;
    display: flex; align-items: center; justify-content: center; gap: 18px;
  }
  .brand-dot {
    width: 62px; height: 62px; border-radius: 50%;
    background: var(--paper);
  }
  .brand-name {
    font-family: "Cinzel", Georgia, serif;
    font-weight: 400;
    line-height: 1;
  }
  .front-brand .brand-name { color: var(--paper); }
  .brand-name .line-1 { display: block; font-size: 50px; letter-spacing: 1px; }
  .brand-name .line-2 { display: block; font-size: 26px; letter-spacing: 2px; margin-top: 4px; }
  .front-web {
    position: absolute; left: 0; right: 0; top: 200px;
    text-align: center; font-size: 12px; letter-spacing: 0.3px;
    padding-left: 80px;
  }

  /* Back */
  .card-back {
    left: 280px; top: 462px;
    background: var(--paper);
    color: var(--slate);
  }
  .emblem-area {
    position: absolute; left: 28px; top: 46px;
    width: 220px; height: 220px; border-radius: 50%;
    background: radial-gradient(circle at 45% 40%, rgba(0,142,214,0.55), rgba(0,38,73,0.25) 60%, rgba(173,175,170,0.15) 75%, rgba(255,255,255,0) 76%);
  }
  .details {
    position: absolute; right: 34px; top: 34px;
    width: 250px; text-align: right;
  }
  .details .brand-name { color: var(--navy); }
  .details .brand-name .line-1 { font-size: 34px; }
  .details .brand-name .line-2 { font-size: 18px; margin-top: 2px; }
  .rule { height: 1px; background: var(--silver); margin: 12px 0 10px 30px; }
  .person-name { color: var(--mid-blue); font-size: 17px; font-weight: 500; }
  .person-role { font-size: 11px; margin-top: 1px; }
  .address { font-size: 11px; margin-top: 12px; line-height: 1.35; }
  .contact { font-size: 11px; margin-top: 10px; line-height: 1.45; }
  .contact-row { display: flex; justify-content: flex-end; align-items: center; gap: 4px; white-space: nowrap; }
  .contact-row svg { width: 10px; height: 10px; flex: none; }
  .rep-label { color: var(--mid-blue); font-weight: 500; }
</style>
</head>
<body>

  <section class="card card-front" aria-label="Card front">
    <div class="front-brand">
      <span class="brand-dot" aria-hidden="true"></span>
      <span class="brand-name"><span class="line-1">TARLOW</span><span class="line-2">FINANCIAL</span></span>
    </div>
    <p class="front-web">www.tarlowfinancial.example.au</p>
  </section>

  <section class="card card-back" aria-label="Card back">
    <div class="emblem-area" role="img" aria-label="Large brand emblem in blue and grey"></div>
    <div class="details">
      <div class="brand-name"><span class="line-1">TARLOW</span><span class="line-2">FINANCIAL</span></div>
      <div class="rule"></div>
      <p class="person-name">Renata Sollisford</p>
      <p class="person-role">Managing Director</p>
      <p class="address">PO Box 527<br>Larkvale, Victoria, 3999</p>
      <div class="contact">
        <p class="contact-row">0491 738 205
          <svg viewBox="0 0 10 10" aria-hidden="true"><rect width="10" height="10" rx="2" fill="var(--mid-blue)"/><path d="M3 2.5 L4.2 2.5 L4.6 4 L4 4.6 Q4.8 6 5.4 6.2 L6 5.6 L7.5 6 L7.5 7.2 Q4 7.6 2.6 3.2 Z" fill="#fff"/></svg>
        </p>
        <p class="contact-row">r.sollisford@tarlowfinancial.example.au
          <svg viewBox="0 0 10 10" aria-hidden="true"><rect width="10" height="10" rx="2" fill="var(--mid-blue)"/><rect x="2" y="3" width="6" height="4" fill="#fff"/><path d="M2 3 L5 5.3 L8 3" stroke="var(--mid-blue)" stroke-width="0.7" fill="none"/></svg>
        </p>
        <p class="contact-row"><span class="rep-label">Credit Rep No:</span> nnn nnn nnn</p>
      </div>
    </div>
  </section>

</body>
</html>
```